Steadying Downturn Worries

I need a on page electronic flyer for this coaching program. I want a silhouette to accompany the case the copy starts with. I have the copy written but need it put together in a striking way.

Target Market(s)

towards higher net worth individuals

Industry/Entity Type

Electronic

```html
<!DOCTYPE html>
<html lang="en">
<head>
<meta charset="utf-8">
<title>Steadying Downturn Worries — Coaching Flyer</title>
<link rel="stylesheet" href="https://fonts.googleapis.com/css2?family=Gentium+Book+Plus:ital,wght@0,400;0,700;1,400&display=swap">
<style>
  :root {
    --blue: #0a87c6;
    --yellow: #fdb515;
    --green: #0ccd0c;
    --red: #d90d0d;
    --black: #000000;
    --white: #ffffff;
    --ink: #111111;
    --rule: #bdbdbd;
    --head-blue: #1a8fc2;
    --head-red: #d81515;
    --head-green: #14c514;
    --badge-blue: #4a86c8;
  }
  * { box-sizing: border-box; margin: 0; padding: 0; }
  html, body { width: 848px; height: 1200px; overflow: hidden; background: var(--white); }
  body { font-family: "Gentium Book Plus", "Palatino Linotype", serif; color: var(--ink); }
  .flyer { position: relative; width: 848px; height: 1200px; background: var(--white); }

  .frame-quad { position: absolute; }
  .frame-quad.top-left { left: 53px; top: 53px; width: 371px; height: 539px; background: var(--blue); }
  .frame-quad.top-right { left: 424px; top: 53px; width: 372px; height: 539px; background: var(--yellow); }
  .frame-quad.bottom-left { left: 53px; top: 592px; width: 371px; height: 541px; background: var(--green); }
  .frame-quad.bottom-right { left: 424px; top: 592px; width: 372px; height: 541px; background: var(--red); }

  .sheet { position: absolute; left: 76px; top: 76px; width: 695px; height: 1029px; background: var(--white); }

  .portrait { position: absolute; left: 30px; top: 4px; width: 138px; height: 135px; background: var(--black);
    border-radius: 55px 55px 3px 3px; }
  .portrait-name { position: absolute; left: 30px; top: 112px; width: 138px; text-align: center;
    color: var(--white); font-weight: 700; font-size: 13.5px; }

  .headline { position: absolute; left: 162px; width: 520px; text-align: center; font-weight: 700; }
  .headline.kicker { top: 35px; color: var(--head-blue); font-size: 16.5px; }
  .headline.title { top: 80px; color: var(--head-red); font-size: 15.5px; }
  .headline.subtitle { top: 104px; color: var(--head-green); font-size: 15.5px; }
  .head-rule { position: absolute; left: 192px; top: 148px; width: 474px; height: 1px; background: var(--rule); }

  .copy { position: absolute; left: 8px; width: 676px; font-size: 13.3px; line-height: 19px; }
  .bullets { position: absolute; left: 8px; top: 509px; width: 676px; list-style: none; font-size: 13.3px; }
  .bullets li { position: relative; padding-left: 67px; height: 38px; }
  .bullets li::before { content: ""; position: absolute; left: 30px; top: 6px; width: 6px; height: 6px;
    border-radius: 50%; background: var(--ink); }
  .bio { position: absolute; left: 8px; width: 676px; font-size: 15px; line-height: 21px; }

  .feature-art { position: absolute; left: 7px; top: 873px; width: 538px; height: 148px;
    background: radial-gradient(ellipse at center, #7a3a10 0%, #3a1a08 45%, var(--black) 85%); }

  .brand { position: absolute; left: 555px; top: 900px; width: 140px; text-align: center; }
  .brand-dot { width: 70px; height: 70px; border-radius: 50%; background: var(--badge-blue); margin: 0 auto 8px; }
  .brand-name { color: var(--badge-blue); font-weight: 700; font-size: 17px; }

  .contact { position: absolute; top: 1111px; font-weight: 700; font-size: 13.5px; }
  .contact.phone { left: 83px; color: var(--black); }
  .contact.email { right: 83px; color: var(--white); }
</style>
</head>
<body>
<div class="flyer">
  <div class="frame-quad top-left"></div>
  <div class="frame-quad top-right"></div>
  <div class="frame-quad bottom-left"></div>
  <div class="frame-quad bottom-right"></div>

  <div class="sheet">
    <div class="portrait" role="img" aria-label="Black head-and-shoulders silhouette of the coach"></div>
    <div class="portrait-name">Dana Whitlow</div>

    <p class="headline kicker">Sometimes the best financial advice isn't about numbers...</p>
    <h1 class="headline title">Steadying Downturn Worries:</h1>
    <p class="headline subtitle">From Financial Worries to Wealth Satisfaction</p>
    <div class="head-rule"></div>

    <p class="copy" style="top:160px">A 49 year old attorney, Steve was used to success and rising net worth. But with huge losses in the market crash, layoffs at his firm, his kids heading for college and the stagnant economy stretching ahead, his usual optimism is gone.</p>
    <p class="copy" style="top:207px">With his anxiety growing, Steve doubts his own decision making ability. His confidence slipping, he stopped opening his financial statements and could barely speak to his financial advisor. He thought if his advisor said “hang in there” one more time, he just might blow up.</p>
    <p class="copy" style="top:288px">Yet Steve felt too embarrassed to talk about his deep worries, even with his wife. It seemed like all he could do was pour another glass of wine and suffer in isolation.</p>
    <p class="copy" style="top:336px">If you're like Steve, you're afraid and alone with plenty of company. In a September 2009 Wellbeing Research Council poll, 80 percent reported the economy is causing significant stress, up from 66 percent from the previous April. The Restful Living Institute said 27 percent of people surveyed had sleeplessness because of economic anxiety.</p>
    <p class="copy" style="top:433px">How can you take control of these worries and get back to enjoying your life?</p>
    <p class="copy" style="top:470px">In this 5 session coaching process you will :</p>

    <ul class="bullets">
      <li>Learn a decision making tool to make choices that truly serve your needs</li>
      <li>Clarify and more fully engage with your purpose and passions</li>
      <li>Improve your relationship with your financial advisor</li>
      <li>Feel more in control and confident in your financial life</li>
    </ul>

    <p class="copy" style="top:660px">This process guides you to step back and understand the source of your financial worry—your unique story about the meaning of money. Your money story drives your emotions and decision making—for better and worse. You'll learn a decision making tool for more conscious, effective and satisfying financial and life decisions.</p>
    <p class="copy" style="top:731px">You'll also examine your core values and strengths—what really matters most to you and how you work at your best. When you use your money and your core strengths to pursue your highest aspirations, life and wealth become balanced. As you commit more fully to your mission and passions, satisfaction grows and money worries melt away.</p>

    <p class="bio" style="top:804px">Dana Whitlow, Ph.D. is a psychologist with 30 years of experience treating anxiety and stress. She is co-founder and facilitator of Summit Circle, a peer learning group for high net worth investors.</p>

    <div class="feature-art" role="img" aria-label="Decorative colour-block artwork on a black panel"></div>

    <div class="brand">
      <div class="brand-dot"></div>
      <div class="brand-name">Summit Circle</div>
    </div>
  </div>

  <div class="contact phone">Call : 555-014-2287</div>
  <div class="contact email">Email : dana.whitlow@example.com</div>
</div>
</body>
</html>
```